Vivaform - Fitness Coach. Needs a Business Card Design that I can also use for other advertising

Established 2012, I have finished the QPLB National Certificate in Fitness & Personal Training. Harrowgate First Aid Certificate. I have the Auckland 800m track records for MW45. I also came 1st at the 2012 Pacifica Games in 800 & 1500m. I am passionate about health & fitness and would like to help people reach their health & fitness goals. I also take health & fitness weekends. Main interests - Running, Weight Training, Yoga & Aqua Jogging. I like strength/power, but am femine.

Target Market(s)

Male or Female 18 and over that wants to improve their health & fitness

Industry/Entity Type

Advertising

Requirements
Must have
• my name: Lorissa K Dunmore contact details: lori@brightpath.co.nz mobile - 021 579318 URL name: facebook.com/lorissaKdunmore - VivaForm
Photo of Me

```html
<!DOCTYPE html>
<html lang="en">
<head>
<meta charset="utf-8">
<title>Lorissa K Dunmore – Vivaform Fitness Coach</title>
<link rel="stylesheet" href="https://fonts.googleapis.com/css2?family=Tenor+Sans&family=Noto+Sans:wght@400&display=swap">
<style>
  :root {
    --bg-deep: #111111;
    --bg-soft: #1e1e1e;
    --name-green-top: #7fd62a;
    --name-green-bottom: #3f8f0c;
    --rule-green: #4fae14;
    --contact-grey: #8a8a8a;
    --frame-light: #a9a9a9;
    --frame-dark: #4a4a4a;
    --icon-grey: #bdbdbd;
    --photo-foliage: #3f6a26;
    --photo-lawn: #6fa83b;
  }
  html, body {
    margin: 0;
    padding: 0;
    width: 1200px;
    height: 675px;
    overflow: hidden;
    background: var(--bg-deep);
  }
  .card {
    position: relative;
    width: 1200px;
    height: 675px;
    overflow: hidden;
    background:
      radial-gradient(ellipse 60% 55% at 55% 40%, var(--bg-soft) 0%, var(--bg-deep) 75%);
  }
  .portrait-frame {
    position: absolute;
    left: 50px;
    top: 52px;
    width: 328px;
    height: 550px;
    box-sizing: border-box;
    padding: 7px;
    background: linear-gradient(180deg, var(--frame-light), var(--frame-dark));
  }
  .portrait {
    width: 100%;
    height: 100%;
    background: linear-gradient(180deg, var(--photo-foliage) 0%, #2f5a1c 55%, #4f8a2a 68%, var(--photo-lawn) 78%, #7cb846 100%);
  }
  .name {
    position: absolute;
    right: 58px;
    top: 100px;
    margin: 0;
    font-family: "Tenor Sans", sans-serif;
    font-weight: 400;
    font-size: 64px;
    line-height: 1;
    letter-spacing: 0.5px;
    background: linear-gradient(180deg, var(--name-green-top), var(--name-green-bottom));
    -webkit-background-clip: text;
    background-clip: text;
    color: transparent;
    white-space: nowrap;
  }
  .contact {
    position: absolute;
    right: 58px;
    margin: 0;
    font-family: "Noto Sans", sans-serif;
    font-size: 40px;
    line-height: 1;
    color: var(--contact-grey);
    white-space: nowrap;
  }
  .mobile { top: 196px; font-size: 41px; }
  .divider {
    position: absolute;
    left: 712px;
    top: 434px;
    width: 432px;
    height: 2px;
    background: var(--rule-green);
  }
  .email { top: 455px; font-size: 36px; }
  .social {
    position: absolute;
    right: 55px;
    top: 512px;
    display: flex;
    align-items: center;
    gap: 26px;
  }
  .social-mark {
    width: 56px;
    height: 56px;
    border-radius: 6px;
    background: var(--icon-grey);
  }
  .social-name {
    font-family: "Noto Sans", sans-serif;
    font-size: 36px;
    color: var(--contact-grey);
  }
</style>
</head>
<body>
  <main class="card">
    <div class="portrait-frame">
      <div class="portrait" role="img" aria-label="Photo of the fitness coach jumping in the air in front of a green hedge on a lawn"></div>
    </div>

    <h1 class="name">Lorissa K Dunmore</h1>
    <p class="contact mobile">Mobile - 021 579318</p>

    <div class="divider"></div>

    <p class="contact email">lori@brightpath.co.nz</p>
    <div class="social">
      <span class="social-mark"></span>
      <span class="social-name">Vivaform</span>
    </div>
  </main>
</body>
</html>
```